Design an Elegant Handbag Brand website

I need a webiste design are looking for ideas for a new theme, color scheme, etc. You come up with the general look and feel of the home page and our team will take it from there.
We're only looking for a one (1) page layout which should be fashionable and graphic intensive, but also include the standard homepage links (about us, see our collections, etc)

Target Market(s)

Our customers are fashionable women looking for an animal friendly and environmentally friendly handbag.

Industry/Entity Type

Business

Number of Pages Required

1 page

Font styles to use
Serif
Sans Serif

Requirements
Must have
• Feel free to modify it with different colors or tweaks as you see fit. We are open to all suggestions.
Nice to have

```html
<!DOCTYPE html>
<html lang="en">
<head>
<meta charset="utf-8">
<title>Lune &amp; Leaf — Handbags</title>
<link href="https://fonts.googleapis.com/css2?family=Raleway:wght@400;500;600;700&family=Lato:wght@400;700&display=swap" rel="stylesheet">
<style>
:root{
  --pink:#ec2e82;
  --teal:#137f8c;
  --ink:#2b2b2b;
  --muted:#555;
  --line:#e3e3e3;
  --dark:#2b2b2b;
  --white:#fff;
}
*{box-sizing:border-box;margin:0;padding:0}
html,body{width:1200px;height:3476px;overflow:hidden}
body{position:relative;font-family:'Lato',sans-serif;color:var(--ink);background:var(--white)}
.abs{position:absolute}
.photo{position:absolute}
/* header */
.nav{left:72px;top:60px;display:flex;gap:25px;font:500 13px 'Raleway',sans-serif;letter-spacing:.3px}
.nav a{color:var(--ink);text-decoration:none}
.nav a.active{color:var(--teal);border-bottom:2px solid var(--teal);padding-bottom:8px}
.brand{left:0;width:1200px;top:58px;text-align:center;font:700 22px 'Raleway',sans-serif;color:var(--teal);letter-spacing:1px}
.brand-sub{left:0;width:1200px;top:88px;text-align:center;font:400 8px 'Lato',sans-serif;letter-spacing:3px;color:var(--muted)}
.icons{right:70px;top:54px;display:flex;gap:22px}
/* hero */
.hero{left:0;top:119px;width:1200px;height:517px;background:linear-gradient(90deg,#2c6c96 0%,#5c94b8 45%,#9aa9b4 70%,#6b86a6 100%)}
.hero-frame{left:184px;top:235px;width:202px;height:268px;border:2px solid var(--white);border-top-width:2px}
.hero-off{left:178px;top:256px;font:700 50px 'Raleway',sans-serif;color:var(--white)}
.hero-h{left:179px;top:311px;font:500 29px 'Raleway',sans-serif;color:var(--white);letter-spacing:.5px}
.hero-p{left:181px;top:350px;width:420px;font:400 12px/1.25 'Lato',sans-serif;color:var(--white)}
.btn{display:flex;align-items:stretch;height:40px;font:500 13px 'Raleway',sans-serif;color:var(--white)}
.btn .t{background:var(--pink);display:flex;align-items:center;padding:0 24px}
.btn .c{background:var(--teal);width:50px;display:flex;align-items:center;justify-content:center}
.hero-dots{left:1162px;top:360px}
.hero-tab{left:566px;top:612px;width:68px;height:24px;background:var(--white);border-radius:34px 34px 0 0}
/* categories */
.cat{top:671px;width:358px;height:198px}
.cat span{position:absolute;left:0;width:100%;top:88px;text-align:center;font:500 25px 'Raleway',sans-serif;color:var(--white)}
.cat b{position:absolute;left:24px;bottom:14px;color:var(--white);font:700 16px 'Lato',sans-serif}
.arrow{width:34px;height:34px;border-radius:50%;background:var(--white);box-shadow:0 1px 5px rgba(0,0,0,.25);display:flex;align-items:center;justify-content:center}
/* titles */
.title{left:0;width:1200px;text-align:center;font:400 29px 'Raleway',sans-serif;color:var(--ink)}
.tabs{left:399px;top:978px;display:flex;gap:46px;font:400 13px 'Lato',sans-serif;color:var(--ink)}
.tabs .on{color:var(--teal)}
.card{top:1037px;width:249px;height:268px;border:1px solid var(--line);background:var(--white)}
.card.lift{box-shadow:0 2px 10px rgba(0,0,0,.18)}
.card .photo{left:30px;top:20px;width:187px;height:228px;border-radius:20px}
.pname{top:1330px;width:249px;text-align:center;font:400 14px 'Lato',sans-serif;color:var(--muted)}
.price{top:1350px;width:249px;text-align:center;font:700 16px 'Lato',sans-serif;color:#b20e12}
.browse{width:157px;height:40px;background:var(--pink);color:var(--white);font:500 13px 'Raleway',sans-serif;display:flex;align-items:center;justify-content:center}
/* sale */
.sale{left:0;top:1519px;width:1200px;height:511px;background:linear-gradient(90deg,#34433b 0%,#4e6b60 40%,#5d7896 70%,#3a5066 100%)}
.sale-frame{left:16px;top:1537px;width:1170px;height:476px;border:1px solid rgba(255,255,255,.6)}
.sale-h{left:109px;top:1645px;font:600 60px 'Raleway',sans-serif;color:var(--white)}
.sale-s{left:111px;top:1717px;font:400 28px/1.05 'Raleway',sans-serif;color:var(--white)}
.sale-p{left:111px;top:1792px;font:400 13px 'Lato',sans-serif;color:var(--white)}
/* blog */
.post{top:2172px;width:329px;height:382px;border:1px solid var(--line)}
.post .photo{left:0;top:0;width:100%;height:200px}
.post .d{position:absolute;left:20px;top:212px;font:400 13px 'Lato',sans-serif;color:var(--muted)}
.post h3{position:absolute;left:20px;top:236px;font:500 15px 'Raleway',sans-serif}
.post hr{position:absolute;left:20px;top:263px;width:27px;border:0;border-top:2px solid var(--teal)}
.post p{position:absolute;left:20px;top:280px;width:292px;font:400 12.5px/1.45 'Lato',sans-serif;color:var(--muted)}
.post a{position:absolute;left:20px;top:352px;font:400 13px 'Lato',sans-serif;color:var(--teal)}
/* about */
.about-img{left:50px;top:2727px;width:600px;height:270px;background:radial-gradient(ellipse at center,#8c919a 0%,#c9ccd0 45%,#fff 72%)}
.about-k{left:682px;top:2734px;font:500 13px 'Raleway',sans-serif;letter-spacing:.4px;color:var(--muted)}
.about-p{left:682px;width:400px;font:400 12.5px/1.2 'Lato',sans-serif;color:var(--muted)}
/* features */
.feat{top:3075px;width:252px;height:102px;border:1px solid var(--line);display:flex;align-items:center;gap:12px;padding-left:14px}
.feat h4{font:500 16px 'Raleway',sans-serif}
.feat small{font:400 12px 'Lato',sans-serif;color:var(--muted)}
/* footer */
.foot{top:3229px;height:177px}
.fh{font:500 14px 'Raleway',sans-serif;color:var(--white);text-align:center;margin-top:46px}
.social{display:flex;gap:10px;justify-content:center;margin-top:14px}
.social i{width:30px;height:30px;border-radius:50%;border:1px solid var(--white)}
.social i.f{background:var(--white)}
.ql{display:flex;justify-content:center;gap:10px;margin-top:20px;font:500 13px 'Raleway',sans-serif;color:var(--white)}
.cards{display:flex;gap:10px;justify-content:center;margin-top:16px}
.cards i{width:36px;height:22px;border-radius:2px;background:var(--white)}
.contact{text-align:center;font:400 12.5px/1.7 'Lato',sans-serif;color:var(--white);margin-top:10px}
.copy{left:0;top:3433px;width:1200px;text-align:center;font:400 13px 'Lato',sans-serif;color:var(--ink)}
.copy b{font-weight:400;color:var(--pink)}
</style>
</head>
<body>

<header>
  <nav class="abs nav"><a class="active">HOME</a><a>PRODUCTS</a><a>BLOG</a><a>ABOUT</a><a>CONTACT</a></nav>
  <div class="abs brand">LUNE &amp; LEAF</div>
  <div class="abs brand-sub">YOUR TAGLINE HERE</div>
  <div class="abs icons">
    <svg width="16" height="16" viewBox="0 0 16 16" fill="none" stroke="#333" stroke-width="1.6"><circle cx="7" cy="7" r="5"/><path d="M11 11l4 4"/></svg>
    <svg width="16" height="16" viewBox="0 0 16 16" fill="none" stroke="#333" stroke-width="1.5"><circle cx="8" cy="5" r="3.5"/><path d="M2 15c0-4 3-6 6-6s6 2 6 6"/></svg>
    <svg width="17" height="16" viewBox="0 0 17 16" fill="none" stroke="#333" stroke-width="1.5"><path d="M8.5 14.5S1.5 10 1.5 5.3A3.6 3.6 0 0 1 8.5 4a3.6 3.6 0 0 1 7 1.3c0 4.7-7 9.2-7 9.2z"/></svg>
    <svg width="20" height="18" viewBox="0 0 20 18" fill="none" stroke="#333" stroke-width="1.5"><path d="M1 2h3l2 10h10l2-7H5"/><circle cx="8" cy="15.5" r="1.3"/><circle cx="15" cy="15.5" r="1.3"/><circle cx="16" cy="3" r="3" fill="#ec2e82" stroke="none"/></svg>
  </div>
</header>

<section>
  <div class="photo hero" role="img" aria-label="Woman in blue jeans carrying a tan leather handbag by the sea"></div>
  <div class="abs hero-frame"></div>
  <div class="abs hero-off">25% OFF</div>
  <div class="abs hero-h">QUALITY IN EVERY DESIGN</div>
  <p class="abs hero-p">Lorem ipsum dolor sit amet, consectetur adipiscing elit, sed tempor incididunt ut labore et dolore magna aliqua.</p>
  <div class="abs btn" style="left:205px;top:440px"><span class="t">SHOP NOW</span><span class="c"><svg width="18" height="16" viewBox="0 0 20 18" fill="none" stroke="#fff" stroke-width="1.5"><path d="M1 2h3l2 10h10l2-7H5"/><circle cx="8" cy="15.5" r="1.3"/><circle cx="15" cy="15.5" r="1.3"/></svg></span></div>
  <svg class="abs hero-dots" width="20" height="60" viewBox="0 0 20 60"><g fill="#fff" opacity=".7"><circle cx="4" cy="4" r="2"/><circle cx="4" cy="16" r="2.6" opacity="1"/><circle cx="4" cy="28" r="2"/><circle cx="4" cy="40" r="2"/></g><path d="M8 16h12" stroke="#fff"/></svg>
  <div class="abs hero-tab"><svg width="68" height="24" viewBox="0 0 68 24" fill="none" stroke="#555" stroke-width="1.2"><path d="M30 8l4 4 4-4M30 13l4 4 4-4"/></svg></div>
</section>

<section>
  <div class="abs cat" style="left:35px"><div class="photo" style="inset:0;background:linear-gradient(135deg,#6e7a80,#2f4c4a 50%,#9a8a7c)" role="img" aria-label="Woman holding a green shoulder bag"></div><span>SHOULDER</span><b>&gt;&gt;</b></div>
  <div class="abs cat" style="left:423px"><div class="photo" style="inset:0;background:linear-gradient(135deg,#8a6d58,#3f332e 50%,#b3a19a)" role="img" aria-label="Woman wearing a brown crossbody bag"></div><span>CROSSBODY</span><b>&gt;&gt;</b></div>
  <div class="abs cat" style="left:810px"><div class="photo" style="inset:0;background:linear-gradient(135deg,#6b4a3a,#c49a8e 50%,#9a6f5c)" role="img" aria-label="Hands holding a floral clutch"></div><span>CLUTCHES</span><b>&gt;&gt;</b></div>
  <div class="abs arrow" style="left:18px;top:757px"><svg width="10" height="10" viewBox="0 0 10 10" fill="none" stroke="#333" stroke-width="1.4"><path d="M6.5 1.5L3 5l3.5 3.5"/></svg></div>
  <div class="abs arrow" style="left:1149px;top:757px"><svg width="10" height="10" viewBox="0 0 10 10" fill="none" stroke="#333" stroke-width="1.4"><path d="M3.5 1.5L7 5 3.5 8.5"/></svg></div>
</section>

<section>
  <h2 class="abs title" style="top:928px">FEATURE PRODUCTS</h2>
  <div class="abs tabs"><span class="on">ALL</span><span>NEW ARRIVAL</span><span>BEST SELLER</span><span>DISCOUNTED</span></div>
  <div class="abs arrow" style="left:1048px;top:966px;box-shadow:0 1px 4px rgba(0,0,0,.12)"><svg width="10" height="10" viewBox="0 0 10 10" fill="none" stroke="#bbb" stroke-width="1.4"><path d="M6.5 1.5L3 5l3.5 3.5"/></svg></div>
  <div class="abs arrow" style="left:1091px;top:966px;background:var(--teal)"><svg width="10" height="10" viewBox="0 0 10 10" fill="none" stroke="#fff" stroke-width="1.6"><path d="M3.5 1.5L7 5 3.5 8.5"/></svg></div>

  <div class="abs card" style="left:72px"><div class="photo" style="background:linear-gradient(#f3d3d3,#d4141e)" role="img" aria-label="Red leather handbag"></div></div>
  <div class="abs card lift" style="left:340px"><div class="photo" style="background:linear-gradient(#f3e6f0,#c995c9)" role="img" aria-label="Lilac handbag with gold handles"></div>
    <svg class="abs" style="left:66px;top:134px" width="118" height="34" viewBox="0 0 118 34"><g fill="#fff"><circle cx="17" cy="17" r="16"/><circle cx="59" cy="17" r="16"/><circle cx="101" cy="17" r="16"/></g><g fill="none" stroke="#137f8c" stroke-width="1.3"><path d="M9 11h2l2 7h7l1.5-5H12"/><circle cx="14" cy="21" r="1"/><circle cx="19" cy="21" r="1"/><path d="M59 23s-5-3-5-6.5a2.5 2.5 0 0 1 5-.8 2.5 2.5 0 0 1 5 .8c0 3.5-5 6.5-5 6.5z"/><circle cx="97" cy="17" r="1.8"/><circle cx="105" cy="12" r="1.8"/><circle cx="105" cy="22" r="1.8"/><path d="M98.6 16l4.8-3M98.6 18l4.8 3"/></g></svg>
  </div>
  <div class="abs card" style="left:608px"><div class="photo" style="background:linear-gradient(#dbe8f6,#3f7fcf)" role="img" aria-label="Blue nylon hobo bag"></div></div>
  <div class="abs card" style="left:876px"><div class="photo" style="background:linear-gradient(#fbe0d2,#f35b18)" role="img" aria-label="Orange leather tote bag"></div></div>

  <div class="abs pname" style="left:72px">PRODUCT NAME</div><div class="abs price" style="left:72px">$25.00</div>
  <div class="abs pname" style="left:340px">PRODUCT NAME</div><div class="abs price" style="left:340px">$25.00</div>
  <div class="abs pname" style="left:608px">PRODUCT NAME</div><div class="abs price" style="left:608px">$25.00</div>
  <div class="abs pname" style="left:876px">PRODUCT NAME</div><div class="abs price" style="left:876px">$25.00</div>

  <div class="abs browse" style="left:521px;top:1412px">BROWSE MORE</div>
</section>

<section>
  <div class="photo sale" role="img" aria-label="Woman in white shirt and jeans seated outdoors with a mustard tote bag"></div>
  <div class="abs sale-frame"></div>
  <div class="abs sale-h">BIG SALE</div>
  <div class="abs sale-s">Get upto 20% Off Discount<br>on Your 1st Order</div>
  <div class="abs sale-p">Lorem ipsum dolor sit amet, consectetur adipiscing elit sed</div>
  <div class="abs btn" style="left:112px;top:1830px"><span class="t">SHOP NOW</span><span class="c"><svg width="18" height="16" viewBox="0 0 20 18" fill="none" stroke="#fff" stroke-width="1.5"><path d="M1 2h3l2 10h10l2-7H5"/><circle cx="8" cy="15.5" r="1.3"/><circle cx="15" cy="15.5" r="1.3"/></svg></span></div>
</section>

<section>
  <h2 class="abs title" style="top:2112px">LATEST BLOG</h2>
  <article class="abs post" style="left:72px"><div class="photo" style="background:linear-gradient(135deg,#d0d0cc,#e8cfc9 55%,#9c9c98)" role="img" aria-label="Woman in pink jacket leaning on a stone wall"></div><span class="d">11 May, 2020</span><h3>Blog Heading 01</h3><hr><p>Lorem Ipsum is simply dummy text of the printing and typesetting industry. Lorem Ipsum has been standard dummy text ever since the 1500s,</p><a>Read More</a></article>
  <article class="abs post" style="left:435px"><div class="photo" style="background:linear-gradient(135deg,#9c7a66,#c39a7c 50%,#5a4a42)" role="img" aria-label="Woman in camel coat carrying a black bag"></div><span class="d">11 May, 2020</span><h3>Blog Heading 01</h3><hr><p>Lorem Ipsum is simply dummy text of the printing and typesetting industry. Lorem Ipsum has been standard dummy text ever since the 1500s,</p><a>Read More</a></article>
  <article class="abs post" style="left:795px"><div class="photo" style="background:linear-gradient(135deg,#3c4c46,#d9d8d4 50%,#6f7070)" role="img" aria-label="White handbag and sunglasses on a ledge"></div><span class="d">11 May, 2020</span><h3>Blog Heading 01</h3><hr><p>Lorem Ipsum is simply dummy text of the printing and typesetting industry. Lorem Ipsum has been standard dummy text ever since the 1500s,</p><a>Read More</a></article>
  <div class="abs browse" style="left:521px;top:2593px">BROWSE MORE</div>
</section>

<section>
  <h2 class="abs title" style="top:2676px">ABOUT US</h2>
  <div class="abs" style="left:587px;top:2722px;width:27px;border-top:2px solid var(--teal)"></div>
  <div class="photo about-img" role="img" aria-label="Group of black, grey and white satchel bags with flowers"></div>
  <div class="abs about-k">QUALITY IN EVERY DESIGN</div>
  <p class="abs about-p" style="top:2768px">Lorem Ipsum is simply dummy text of the printing and typesetting industry has been the industry's standard dummy text ever since the 1500s,</p>
  <p class="abs about-p" style="top:2829px">when an unknown printer took a galley of type and scrambled it to make a type specimen book. It has survived not only five centuries, but also the leap into electronic typesetting, remaining essentially unchanged. It was popularised in the 1960s</p>
  <div class="abs browse" style="left:682px;top:2925px">READ MORE</div>
</section>

<section>
  <div class="abs feat" style="left:72px"><svg width="62" height="40" viewBox="0 0 62 40" fill="none" stroke="#333" stroke-width="1.5"><rect x="10" y="6" width="30" height="24"/><path d="M40 14h10l8 8v8H40M2 12h6M0 18h8"/><circle cx="18" cy="33" r="4"/><circle cx="48" cy="33" r="4"/></svg><div><h4>Fast &amp; Free Shipping</h4><small>on order Over $90</small></div></div>
  <div class="abs feat" style="left:339px"><svg width="50" height="44" viewBox="0 0 50 44" fill="none" stroke="#333" stroke-width="1.5"><path d="M8 24v-6a17 17 0 0 1 34 0v6"/><rect x="4" y="22" width="8" height="12" rx="3"/><rect x="38" y="22" width="8" height="12" rx="3"/><path d="M42 34c0 5-6 7-12 7"/></svg><div><h4>Save 25% When You</h4><small>Call&nbsp; +000 555 019</small></div></div>
  <div class="abs feat" style="left:605px"><svg width="50" height="44" viewBox="0 0 50 44" fill="none" stroke="#333" stroke-width="1.5"><rect x="8" y="16" width="34" height="24"/><rect x="5" y="10" width="40" height="6"/><path d="M25 10v30M25 10c-4-8-12-6-8 0M25 10c4-8 12-6 8 0"/></svg><div><h4>Online Help Support</h4><small>Sign up For Gifts</small></div></div>
  <div class="abs feat" style="left:872px"><svg width="56" height="44" viewBox="0 0 56 44" fill="none" stroke="#333" stroke-width="1.5"><path d="M10 22c0-9 8-14 18-14s18 5 18 14-6 12-10 13v6h-6v-4h-6v4h-6v-6c-4-2-8-6-8-13z"/><circle cx="36" cy="10" r="7"/><path d="M36 6v8M32 10h8M4 20l6 2"/></svg><div><h4>15-Day Money Back</h4><small>on order Over $90</small></div></div>
</section>

<footer>
  <div class="abs foot" style="left:0;width:413px;background:var(--pink)">
    <div class="fh">FOLLOW US</div>
    <div class="social"><i class="f"></i><i></i><i></i></div>
  </div>
  <div class="abs foot" style="left:413px;width:394px;background:var(--teal)">
    <div class="fh">QUICK LINKS</div>
    <div class="ql"><span>HOME</span>|<span>PRODUCTS</span>|<span>BLOG</span>|<span>ABOUT</span>|<span>CONTACT</span></div>
    <div class="cards"><i></i><i></i><i></i><i></i><i></i></div>
  </div>
  <div class="abs foot" style="left:807px;width:393px;background:var(--dark)">
    <div class="fh">CONTACT US</div>
    <div class="contact">
      <svg width="9" height="12" viewBox="0 0 9 12"><path d="M4.5 0A4.5 4.5 0 0 0 0 4.5C0 8 4.5 12 4.5 12S9 8 9 4.5A4.5 4.5 0 0 0 4.5 0z" fill="#fff"/><circle cx="4.5" cy="4.5" r="1.6" fill="#2b2b2b"/></svg> 48 Orchard Row, Maple Hollow,<br>OR 90210<br>
      <svg width="11" height="11" viewBox="0 0 11 11"><path d="M2 0l2 3-1 1.5c.8 1.6 2 2.8 3.5 3.5L8 7l3 2-1 2C5 11 0 6 0 1z" fill="#fff"/></svg> +000 555 010 2<br>
      <svg width="12" height="9" viewBox="0 0 12 9"><rect width="12" height="9" fill="#fff"/><path d="M0 0l6 5 6-5" stroke="#2b2b2b" fill="none"/></svg> hello@luneleaf.example
    </div>
  </div>
  <div class="abs copy">COPYRIGHT © <b>LUNE &amp; LEAF</b>,&nbsp; ALL RIGHTS RESERVED.</div>
</footer>

</body>
</html>
```